Etiketten-Design für Weißen Spritzwein
Zielgruppe
Weingut
Aufgabenstellung
Wir benötigen ein Etikett für einen Weißen Spritzwein in der Flasche 0,33.
Das Etikett soll erfrischend, spritzig, ansprechend und modern sein.
Das Wort 'Weißer Spritzer' soll groß darauf zu sehen sein. (Wobei 'Weißer' nur klein und 'Spritzer' GROß!
Unser Logo + Kohlensäureblasen bitte auch hinzufügen.
Der Schriftzug 'weißer Spritzer' + Kohlensäureblasen werden beim Druck mit einer glänzenden Folie veredelt.
Das Format des Etiketts ist 180x80. (Links und rechts stehen Infos vom Wein - nur mittelfläche Designen)
Im Anhang finden sie das Flaschenformat sowie das Etikett + Logo.

```html
<!DOCTYPE html>
<html lang="de">
<head>
<meta charset="utf-8">
<title>Weisser Spritzer – Etikett</title>
<link rel="stylesheet" href="https://fonts.googleapis.com/css2?family=Kaushan+Script&family=Poppins:wght@400&display=swap">
<style>
  :root {
    --stage: #dce3d9;
    --mint-light: #c2e3cb;
    --mint: #b6dabb;
    --mint-deep: #aed6a9;
    --paper: #ffffff;
    --ink: #1d1d1d;
    --gloss-shadow: #f1b79a;
  }
  html, body {
    margin: 0;
    padding: 0;
    width: 1200px;
    height: 807px;
    overflow: hidden;
    background: var(--stage);
  }
  .canvas {
    position: relative;
    width: 1200px;
    height: 807px;
    background: var(--stage);
  }
  .label {
    position: absolute;
    left: 60px;
    top: 163px;
    width: 1080px;
    height: 480px;
    overflow: hidden;
    box-shadow: 0 2px 10px rgba(0, 0, 0, 0.06);
  }
  .label__surface {
    position: absolute;
    inset: 0;
    background: linear-gradient(160deg, var(--mint-light) 0%, var(--mint) 50%, var(--mint-deep) 100%);
  }
  .bubbles {
    position: absolute;
    inset: 0;
    width: 1080px;
    height: 480px;
  }
  .bubbles circle {
    fill: none;
    stroke: var(--paper);
    stroke-width: 2;
    opacity: 0.85;
  }
  .label__center {
    position: absolute;
    left: 340px;
    width: 400px;
    top: 0;
    height: 480px;
    text-align: center;
  }
  .brand-box {
    position: absolute;
    left: 120px;
    top: 28px;
    width: 160px;
    height: 150px;
    background: var(--paper);
    display: flex;
    flex-direction: column;
    align-items: center;
    justify-content: center;
    gap: 6px;
  }
  .brand-box__dot {
    width: 26px;
    height: 26px;
    border-radius: 50%;
    background: var(--ink);
  }
  .brand-box__name,
  .brand-box__sub {
    font-family: "Poppins", sans-serif;
    font-weight: 400;
    color: var(--ink);
    margin: 0;
  }
  .brand-box__name {
    font-size: 21px;
    line-height: 1;
  }
  .brand-box__sub {
    font-size: 8px;
    letter-spacing: 3px;
  }
  .product-kind {
    position: absolute;
    left: 0;
    right: 0;
    top: 210px;
    margin: 0;
    font-family: "Poppins", sans-serif;
    font-weight: 400;
    font-size: 16px;
    letter-spacing: 6px;
    color: var(--paper);
  }
  .product-name {
    position: absolute;
    left: -40px;
    right: -40px;
    top: 234px;
    margin: 0;
    font-family: "Kaushan Script", cursive;
    font-weight: 400;
    font-size: 112px;
    line-height: 1.1;
    color: var(--paper);
    text-shadow: 2px 3px 0 var(--gloss-shadow);
  }
</style>
</head>
<body>
  <main class="canvas">
    <section class="label">
      <div class="label__surface"></div>
      <svg class="bubbles" viewBox="0 0 1080 480" aria-hidden="true">
        <circle cx="372" cy="38" r="5"/>
        <circle cx="390" cy="96" r="6"/>
        <circle cx="404" cy="120" r="4"/>
        <circle cx="372" cy="150" r="5"/>
        <circle cx="412" cy="170" r="3"/>
        <circle cx="372" cy="200" r="8"/>
        <circle cx="352" cy="240" r="4"/>
        <circle cx="412" cy="236" r="3"/>
        <circle cx="360" cy="296" r="7"/>
        <circle cx="386" cy="330" r="3"/>
        <circle cx="372" cy="400" r="6"/>
        <circle cx="430" cy="440" r="4"/>
        <circle cx="702" cy="40" r="8"/>
        <circle cx="690" cy="70" r="5"/>
        <circle cx="708" cy="100" r="3"/>
        <circle cx="662" cy="118" r="5"/>
        <circle cx="720" cy="160" r="4"/>
        <circle cx="680" cy="196" r="4"/>
        <circle cx="694" cy="216" r="10"/>
        <circle cx="668" cy="240" r="3"/>
        <circle cx="652" cy="250" r="4"/>
        <circle cx="720" cy="270" r="4"/>
        <circle cx="700" cy="330" r="3"/>
        <circle cx="612" cy="420" r="5"/>
        <circle cx="638" cy="434" r="3"/>
        <circle cx="500" cy="412" r="5"/>
        <circle cx="250" cy="120" r="6"/>
        <circle cx="200" cy="260" r="5"/>
        <circle cx="300" cy="380" r="4"/>
        <circle cx="820" cy="90" r="5"/>
        <circle cx="860" cy="300" r="6"/>
        <circle cx="780" cy="400" r="4"/>
      </svg>
      <div class="label__center">
        <div class="brand-box">
          <span class="brand-box__dot"></span>
          <p class="brand-box__name">Hollerbach</p>
          <p class="brand-box__sub">WEINGUT</p>
        </div>
        <p class="product-kind">WEISSER</p>
        <h1 class="product-name">Spritzer</h1>
      </div>
    </section>
  </main>
</body>
</html>
```